A Military/Intel consulting firm needs a web design.

We are a niche consulting business that specializes in assisting customers get business with the Military and Intelligence agencies.

Accelerate Growth
Accelerate Time to Market
Focused Acceleration
A GROWING TEAM OF INNOVATIVE, TENACIOUS THINKERS WHO THRIVE ON SOLVING COMPLICATED PROBLEMS.
Intelligence Based Due Diligence

Target Market(s)

Technology, engineering, Unmanned Aerial Vehicle (UAV) companies and satellite operators

Industry/Entity Type

Information Technology

Coding

Coded - Design and coding required

Number of Pages Required

3 page

Requirements
Must have
• We are consultants that identify small companies that can use our services to sell in to mainly Harbor Readiness Directorate or US intelligence agency.
Nice to have
• I like the feel of this site: http://quillbrookpartners.example/
Should not have
• None come to mind

```html
<!DOCTYPE html>
<html lang="en">
<head>
<meta charset="utf-8">
<title>Sierra Vale Group</title>
<link rel="stylesheet" href="https://fonts.googleapis.com/css2?family=Exo+2:wght@500;600;700&family=Roboto:wght@400;500&display=swap">
<style>
:root{
  --navy:#0d3a66;
  --navy-deep:#0a2f55;
  --steel:#a9bcd6;
  --steel-dark:#6f8fb8;
  --ink:#1c1c1c;
  --muted:#777;
  --panel:#f4f4f4;
  --footer:#575757;
  --white:#fff;
}
*{margin:0;padding:0;box-sizing:border-box}
html,body{width:1200px;height:2740px;overflow:hidden;background:var(--white)}
body{font-family:"Roboto",Arial,sans-serif;color:var(--ink);position:relative}
.abs{position:absolute}
.heading{font-family:"Exo 2",Arial,sans-serif;font-weight:600;color:var(--navy);text-transform:uppercase;font-size:17px;letter-spacing:.3px;text-align:center;width:100%}
.rule{width:58px;height:4px;background:var(--steel);left:571px}
.copy{font-size:14.5px;line-height:30px;color:var(--muted);text-align:center}

/* header */
.site-header{top:0;left:0;width:1200px;height:193px}
.brand{left:106px;top:110px;display:flex;align-items:center;gap:12px}
.brand-mark{width:46px;height:46px;background:var(--steel-dark);flex:none}
.brand-text{display:flex;flex-direction:column;gap:4px}
.brand-name{font-family:"Exo 2",Arial,sans-serif;font-weight:700;font-size:22px;color:var(--navy);line-height:1}
.brand-tag{font-family:"Exo 2",Arial,sans-serif;font-weight:600;font-size:10px;color:var(--navy);line-height:1;letter-spacing:.2px}
.call{right:104px;top:56px;display:flex;align-items:center;gap:10px;font-size:16px}
.call-number{font-size:23px;color:var(--navy);margin-left:6px;letter-spacing:.5px}
.nav{top:130px;right:104px;display:flex;align-items:center}
.nav a{font-size:17px;color:var(--ink);text-decoration:none;padding:7px 15px;margin-left:19px}
.nav a.active{background:var(--steel);color:var(--white);margin-left:0}

/* hero */
.hero{top:193px;left:0;width:1200px;height:673px;background:linear-gradient(180deg,#9fb2c8 0%,#6d86a3 45%,#3d5576 75%,#9aafc6 100%)}
.hero-points{left:106px;list-style:none}
.hero-points li{font-family:"Exo 2",Arial,sans-serif;font-weight:500;font-size:26px;color:var(--white);height:46px;display:flex;align-items:center;gap:14px}
.hero-points svg{flex:none}
.dots{left:544px;display:flex;gap:8px}
.dots span{width:16px;height:16px;border-radius:50%;background:var(--white)}
.dots span.on{background:transparent;border:3px solid var(--white)}

/* welcome */
.btn-solid{background:var(--steel);color:var(--white);font-size:14px;letter-spacing:.5px;text-align:center;line-height:34px;height:34px}

/* services */
.services{top:1160px;left:0;width:1200px;height:512px;background:var(--panel)}
.services-shade{top:1160px;left:90px;width:1020px;height:22px;background:radial-gradient(ellipse at top,rgba(0,0,0,.13),rgba(0,0,0,0) 70%)}
.service{width:320px;text-align:center}
.service-icon{width:72px;height:72px;border-radius:50%;background:var(--navy);margin:0 auto;display:flex;align-items:center;justify-content:center}
.service-title{font-family:"Exo 2",Arial,sans-serif;font-weight:600;font-size:16px;color:var(--ink);margin-top:32px}
.service .copy{margin-top:14px;font-size:14px;line-height:25px}

/* consulting band */
.band{top:1672px;left:0;width:1200px;height:378px;background:linear-gradient(180deg,#174e80 0%,#0e3f6e 55%,#0b365f 100%)}
.band-text{color:#e8eef5;font-size:14.5px;line-height:30px;text-align:center;left:115px;width:970px}
.btn-outline{border:1.5px solid var(--white);color:var(--white);font-size:14px;letter-spacing:.5px;text-align:center;line-height:40px;height:43px;width:144px;left:528px}

/* clients */
.client-photo{top:2193px;width:458px;height:238px}
.client-title{font-family:"Exo 2",Arial,sans-serif;font-weight:600;font-size:18px;color:var(--navy);text-align:center;width:458px}
.client-copy{width:458px;font-size:13.5px;line-height:28px}

/* footer */
.footer{top:2576px;left:0;width:1200px;height:164px;background:var(--footer);color:var(--white)}
.footer-label{left:106px;top:52px;font-size:12.5px;font-weight:500;letter-spacing:.3px}
.social{left:106px;top:94px;display:flex;gap:20px}
.social span{width:16px;height:16px;border-radius:50%;background:var(--white)}
.footer-nav{right:104px;top:52px;font-size:12.5px;font-weight:500;letter-spacing:.3px;display:flex;gap:10px}
.footer-copy{right:104px;top:92px;font-size:12.5px;font-weight:500;letter-spacing:.3px}
</style>
</head>
<body>

<header class="abs site-header">
  <div class="abs brand">
    <span class="brand-mark"></span>
    <span class="brand-text">
      <span class="brand-name">SIERRA VALE GROUP</span>
      <span class="brand-tag">Field Insight Advisors</span>
    </span>
  </div>
  <div class="abs call">
    <svg width="16" height="16" viewBox="0 0 24 24"><path fill="#1c1c1c" d="M6.6 10.8c1.4 2.8 3.8 5.1 6.6 6.6l2.2-2.2c.3-.3.7-.4 1-.2 1.1.4 2.3.6 3.6.6.6 0 1 .4 1 1V20c0 .6-.4 1-1 1C10.6 21 3 13.4 3 4c0-.6.4-1 1-1h3.5c.6 0 1 .4 1 1 0 1.3.2 2.5.6 3.6.1.3 0 .7-.2 1z"/></svg>
    <span>Call Us</span>
    <span class="call-number">1.900.XXXX.XXX</span>
  </div>
  <nav class="abs nav">
    <a class="active">Home</a>
    <a>About Us</a>
    <a>Services</a>
    <a>Consulting</a>
    <a>Clients</a>
    <a>Contact Us</a>
  </nav>
</header>

<section class="abs hero" role="img" aria-label="Blurred silhouettes of business people walking through a bright glass office lobby, in cool blue tones"></section>
<ul class="abs hero-points" style="top:448px">
  <li><svg width="16" height="16" viewBox="0 0 16 16"><circle cx="8" cy="8" r="8" fill="#fff"/><path d="M6.5 4.5 10 8l-3.5 3.5" stroke="#5d7594" stroke-width="2" fill="none"/></svg>Accelerate Growth</li>
  <li><svg width="16" height="16" viewBox="0 0 16 16"><circle cx="8" cy="8" r="8" fill="#fff"/><path d="M6.5 4.5 10 8l-3.5 3.5" stroke="#5d7594" stroke-width="2" fill="none"/></svg>Accelerate Time to Market</li>
  <li><svg width="16" height="16" viewBox="0 0 16 16"><circle cx="8" cy="8" r="8" fill="#fff"/><path d="M6.5 4.5 10 8l-3.5 3.5" stroke="#5d7594" stroke-width="2" fill="none"/></svg>Focused Acceleration</li>
  <li><svg width="16" height="16" viewBox="0 0 16 16"><circle cx="8" cy="8" r="8" fill="#fff"/><path d="M6.5 4.5 10 8l-3.5 3.5" stroke="#5d7594" stroke-width="2" fill="none"/></svg>Intelligence Based Due Diligence</li>
</ul>
<div class="abs dots" style="top:796px"><span></span><span></span><span class="on"></span><span></span><span></span></div>

<!-- welcome -->
<h2 class="abs heading" style="top:908px">Welcome to our site</h2>
<div class="abs rule" style="top:952px"></div>
<p class="abs copy" style="top:985px;left:150px;width:900px">We are consultants that identify small companies that can use our services to sell in to mainly Harbor Readiness Directorate<br>or US intelligence agency.</p>
<div class="abs btn-solid" style="top:1079px;left:541px;width:118px">READ MORE</div>

<!-- services -->
<section class="abs services"></section>
<div class="abs services-shade"></div>
<h2 class="abs heading" style="top:1216px">Our services</h2>
<div class="abs rule" style="top:1261px"></div>
<p class="abs copy" style="top:1298px;left:150px;width:900px">There are many variations of passages of Lorem Ipsum available, but the majority have suffered alteration in some form, by injected<br>humour. or randomised words which don't look even slightly believable. .</p>

<div class="abs service" style="top:1409px;left:83px">
  <div class="service-icon"><svg width="28" height="28" viewBox="0 0 28 28"><rect x="10" y="4" width="8" height="5" rx="1" fill="none" stroke="#fff" stroke-width="2.2"/><rect x="3" y="8" width="22" height="15" rx="2" fill="#fff"/><rect x="3" y="14" width="22" height="2" fill="#0d3a66"/><rect x="12" y="13" width="4" height="4" fill="#fff"/></svg></div>
  <h3 class="service-title">CONSULTING</h3>
  <p class="copy">Sed ut perspiciatis unde omnis iste natus<br>error sit voluptatem accusantium<br>doloremque laudantium</p>
</div>
<div class="abs service" style="top:1409px;left:440px">
  <div class="service-icon"><svg width="30" height="30" viewBox="0 0 30 30"><circle cx="15" cy="12" r="4" fill="#fff"/><path d="M7 25c0-5 3.5-8 8-8s8 3 8 8z" fill="#fff"/><g stroke="#fff" stroke-width="2"><path d="M15 2v4M5 6l3 3M25 6l-3 3M2 14h4M24 14h4"/></g></svg></div>
  <h3 class="service-title">SPECIAL OPERATIONS</h3>
  <p class="copy">But I must explain to you how all this<br>mistaken idea of denouncing pleasure<br>and praising pain was.</p>
</div>
<div class="abs service" style="top:1409px;left:800px">
  <div class="service-icon"><svg width="28" height="28" viewBox="0 0 28 28"><path d="M8 9h12l-1.5-4h-9z" fill="#fff"/><circle cx="14" cy="13" r="4.5" fill="#fff"/><path d="M4 26c0-6 4.5-8.5 10-8.5s10 2.5 10 8.5z" fill="#fff"/></svg></div>
  <h3 class="service-title">BUSINESS FIRM</h3>
  <p class="copy">At vero eos et accusamus et iusto odio<br>dignissimos ducimus qui blanditiis<br>praesentium.</p>
</div>

<!-- consulting band -->
<section class="abs band" role="img" aria-label="Faint silhouettes of professionals in an office under a deep navy overlay"></section>
<h2 class="abs heading" style="top:1708px;color:#fff">Consulting</h2>
<div class="abs rule" style="top:1752px;background:#fff"></div>
<p class="abs band-text" style="top:1799px">On the other hand, we denounce with righteous indignation and dislike men who are so beguiled and demoralized by the charms of pleasure of the moment, so blinded by desire, that they cannot foresee the painand trouble that are bound to ensue; and equal blame belongs to those who fail in their duty through weakness of will, which is the same as saying through shrinking from toil and pain. These cases are perfectly simple and easy to distinguish. In a free hour, when our power of choice is untram</p>
<div class="abs btn-outline" style="top:1967px">READ MORE</div>

<!-- clients -->
<h2 class="abs heading" style="top:2092px">Our clients</h2>
<div class="abs rule" style="top:2136px"></div>
<div class="abs client-photo" style="left:122px;background:linear-gradient(135deg,#3f4a36 0%,#6b6a4e 50%,#2e3327 100%)" role="img" aria-label="Soldier in helmet aiming a rifle in the field"></div>
<div class="abs client-photo" style="left:615px;background:linear-gradient(135deg,#d9dde3 0%,#8a96a8 45%,#2f3f5c 100%)" role="img" aria-label="Business people shaking hands across a meeting table"></div>
<h3 class="abs client-title" style="top:2455px;left:122px">MILITARY</h3>
<h3 class="abs client-title" style="top:2455px;left:615px">INTELLIGENCE AGENCIES</h3>
<p class="abs copy client-copy" style="top:2487px;left:122px">But I must explain to you how all this mistaken idea of<br>denouncing pleasure and praising pain was.</p>
<p class="abs copy client-copy" style="top:2487px;left:615px">But I must explain to you how all this mistaken idea of<br>denouncing pleasure.</p>

<!-- footer -->
<footer class="abs footer">
  <div class="abs footer-label">FOLLOW US ON</div>
  <div class="abs social" aria-label="Social links"><span></span><span></span><span></span><span></span></div>
  <nav class="abs footer-nav">
    <span>HOME</span><span>\</span><span>ABOUT US</span><span>\</span><span>SERVICES</span><span>\</span><span>CONSULTING</span><span>\</span><span>CLIENTS</span><span>\</span><span>CONTACT US</span>
  </nav>
  <div class="abs footer-copy">COPYRIGHTS © 2015 ALL RIGHTS RESERVED</div>
</footer>

</body>
</html>
```